Clarvento Hand Sanitizer One Page Website

I need someone to make a one page website for us. The site is www.clarvento.com. I quickly created a simple basic page with all the elements (text, picture, table of pricing, pdf links) needed. I need someone to make the webpage look nice, professioonal, and responsive. There are only 2 links on the page pointing to two pdf files, otherwise there is no navigation needed. The product is a hand sanitizer.
Target Market(s)
Government, corporations, hospitals, large companies
Number of Pages Required
1 page
Requirements
Nice to have
- A hero image relating to hand sanitizer products would be really nice
We would like the bulleted items (Active Ingredient 75% Isopropyl Alcohol, etc) to somehow incorporate icons like the attached picture.

```html
<!DOCTYPE html>
<html lang="en">
<head>
<meta charset="utf-8">
<title>Clarvento Hand Sanitizer</title>
<link href="https://fonts.googleapis.com/css2?family=Inter:wght@400;500;600;700&family=Poppins:wght@600;700&display=swap" rel="stylesheet">
<style>
  :root {
    --navy: #0b1a78;
    --ink: #2b2b2b;
    --muted: #3a3a3a;
    --yellow: #ffc60a;
    --row: #e3e3e3;
    --white: #ffffff;
    --brand-blue: #1f8fc9;
  }
  * { margin: 0; padding: 0; box-sizing: border-box; }
  html, body { width: 1110px; height: 1200px; overflow: hidden; background: var(--white); }
  body { position: relative; font-family: "Inter", Arial, sans-serif; color: var(--ink); }

  .hero {
    position: absolute; left: 0; top: 0; width: 1110px; height: 452px;
    background: linear-gradient(180deg, #ffffff 0%, #ffffff 22%, #dcdcdc 55%, #9a9a9a 100%);
  }
  .brand {
    position: absolute; left: 88px; top: 32px; display: flex; align-items: center; gap: 10px;
    font-family: "Poppins", sans-serif; font-weight: 700; font-size: 34px; color: var(--brand-blue);
    letter-spacing: 0.5px;
  }
  .brand-dot { width: 16px; height: 16px; border-radius: 50%; background: var(--brand-blue); }
  .doc-links {
    position: absolute; top: 38px; right: 87px; display: flex; gap: 24px;
    font-size: 13.5px; font-weight: 500;
  }
  .doc-links a { text-decoration: none; }
  .doc-links .compliance { color: var(--navy); }
  .doc-links .sds { color: var(--muted); }
  .doc-links .sep { color: var(--ink); }
  .enquire {
    position: absolute; left: 415px; top: 206px; width: 281px; height: 42px;
    background: var(--navy); color: var(--white); font-size: 14.5px; font-weight: 600;
    display: flex; align-items: center; justify-content: center; gap: 14px; text-decoration: none;
  }

  .product-title {
    position: absolute; left: 88px; top: 503px;
    font-family: "Poppins", sans-serif; font-weight: 700; font-size: 28px; line-height: 34px; color: var(--muted);
  }
  .product-title .accent { color: var(--navy); display: block; }
  .features { position: absolute; left: 88px; top: 637px; list-style: none; font-size: 16px; line-height: 26.3px; color: var(--ink); }
  .features li { position: relative; padding-left: 21px; }
  .features li::before {
    content: ""; position: absolute; left: 0; top: 10px; width: 6px; height: 6px; background: var(--navy);
  }
  .jug {
    position: absolute; left: 740px; top: 498px; width: 270px; height: 392px;
    background: radial-gradient(ellipse at 50% 45%, #b9c3d3 0%, #8d9ab2 55%, #ffffff 78%);
  }

  .stock {
    position: absolute; left: 88px; top: 870px; width: 204px; height: 36px;
    background: var(--yellow); font-size: 16px; font-weight: 600; color: #1c1c1c;
    display: flex; align-items: center; justify-content: center;
  }
  .pricing {
    position: absolute; left: 88px; top: 935px; width: 888px;
    border-collapse: collapse; font-size: 16px;
  }
  .pricing th, .pricing td { text-align: left; padding: 0 13px; border: 2px solid var(--white); }
  .pricing th { background: var(--navy); color: var(--white); height: 36px; font-weight: 600; }
  .pricing td { background: var(--row); height: 34.5px; color: #222; }

  .footer {
    position: absolute; left: 0; top: 1141px; width: 1110px; height: 59px;
    background: var(--navy); color: var(--white); font-size: 18px; font-weight: 600;
    display: flex; align-items: center; justify-content: center;
  }
</style>
</head>
<body>
  <section class="hero" role="img" aria-label="Black and white photo of a hand pressing a pump bottle and dispensing sanitizer gel into an open palm"></section>

  <div class="brand"><span class="brand-dot"></span>Clarvento</div>

  <nav class="doc-links">
    <a class="compliance" href="#">Letter of Compliance</a>
    <span class="sep">|</span>
    <a class="sds" href="#">Safety Data Sheet</a>
  </nav>

  <a class="enquire" href="#">Enquire Now on 555-201-7730
    <svg width="18" height="12" viewBox="0 0 18 12" fill="none" stroke="#fff" stroke-width="1.6"><path d="M1 6h15M11 1l5 5-5 5"/></svg>
  </a>

  <h1 class="product-title">Isopropyl Alcohol Antiseptic<span class="accent">75% Topical Solution</span>Hand Sanitizer</h1>

  <ul class="features">
    <li>Active Ingredient 75% Isopropyl Alcohol</li>
    <li>USDA rated E3 hand sanitizer, FDA drug registration number (60412-318)</li>
    <li>Meets World Health Organization (WHO) guidelines for an<br>effective hand sanitizer</li>
    <li>Available in 1, 5, 55 and 275-gallon packages</li>
    <li>Effective on killing germs without drying out your hands</li>
  </ul>

  <div class="jug" role="img" aria-label="Product photo of a one-gallon Clarvento sanitizer jug with label"></div>

  <div class="stock">In Stock Ready to Ship</div>

  <table class="pricing">
    <colgroup><col style="width:202px"><col style="width:158px"><col style="width:205px"><col style="width:156px"><col style="width:167px"></colgroup>
    <thead>
      <tr><th>Container</th><th>Min Order Qty</th><th>Price ($ Per Gallon)</th><th>Part Number</th><th>Price Per Ounce</th></tr>
    </thead>
    <tbody>
      <tr><td>1 Gallon / 4 per case</td><td>48</td><td>$27.92</td><td>IP4148</td><td>0.218125</td></tr>
      <tr><td>5 Gallon Pail</td><td>36</td><td>$25.86</td><td>IP5400</td><td>0.202031</td></tr>
      <tr><td>55 Gallon Drum</td><td>4</td><td>$22.42</td><td>IP5540</td><td>0.175156</td></tr>
      <tr><td>275 Gallon Tote</td><td>1</td><td>$20.24</td><td>IP2751</td><td>0.158125</td></tr>
    </tbody>
  </table>

  <footer class="footer">Call 555-201-7730 for inquiries</footer>
</body>
</html>
```